Harbourlight Dental Centre Kelvale business cards and presentation folder

dental practice needing innovative black business cards for 2 different dentists witrh appointment details written at the back of the card for the patient.
name of dentists: Dr Anjali R Venkatesan B.D.S., M.P.H (Melb)
Dr. Raj Kalpat B.D.S.

Target Market(s)

professioinal, working class

Industry/Entity Type

Dental Clinic

Contact Information for Business Card

Dr. Raj Kalpat B.D.S.

Font styles to use
Sans Serif

Requirements
Must have
• Front side: logo
• dentist name
• phone number: 07- 5918 2243
• back side: appointment details: date, time,
• Address: 117C, 58 Tarrow Street, Kelvale - 4561, Queensland
• Email: admin@harbourlightdentalkelvale.example.au
• Website: www.harbourlightdental.example.au
• preferable logo colors
Nice to have
• classy look more pleasing

```html
<!DOCTYPE html>
<html lang="en">
<head>
<meta charset="utf-8">
<title>Harbourlight Dental Centre Kelvale – Business Cards</title>
<link rel="stylesheet" href="https://fonts.googleapis.com/css2?family=Crimson+Text:wght@400;600&display=swap">
<style>
  :root {
    --bg: #d9d9d7;
    --sage: #9cc383;
    --sage-text: #8fbf73;
    --ink: #1b1b1b;
    --paper: #f4f3f0;
    --card-black: #1e1d1e;
    --silver: #c9cbcc;
    --dots: #555;
  }
  * { box-sizing: border-box; margin: 0; padding: 0; }
  html, body { width: 1200px; height: 1200px; overflow: hidden; }
  body {
    background: var(--bg);
    font-family: "Crimson Text", "Times New Roman", serif;
    color: var(--ink);
    position: relative;
  }
  .card {
    position: absolute;
    left: 250px;
    width: 700px;
    height: 420px;
    border-radius: 4px;
    box-shadow: 0 6px 18px rgba(0,0,0,.22);
    overflow: hidden;
  }
  /* Back card */
  .card--back { top: 110px; display: flex; }
  .back__info {
    width: 48%;
    background: var(--sage);
    padding: 46px 30px 30px;
    text-align: center;
    border-right: 3px solid var(--ink);
    display: flex;
    flex-direction: column;
    align-items: center;
  }
  .brand-name {
    font-weight: 600;
    text-transform: uppercase;
    letter-spacing: 1px;
    line-height: 1.15;
  }
  .back__info .brand-name {
    font-size: 22px;
    color: var(--ink);
    padding-bottom: 8px;
    border-bottom: 1px solid var(--ink);
    margin-bottom: 26px;
  }
  .contact-item { font-size: 16px; line-height: 1.45; margin-bottom: 18px; }
  .contact-item svg { display: block; margin: 0 auto 6px; }
  .back__appointment {
    flex: 1;
    background: var(--paper);
    padding: 36px 34px 30px;
  }
  .appointment__title {
    font-size: 17px;
    text-transform: uppercase;
    letter-spacing: .5px;
    margin-bottom: 20px;
  }
  .appointment__row {
    display: flex;
    align-items: baseline;
    font-size: 18px;
    color: var(--sage-text);
    height: 50px;
  }
  .appointment__row::before {
    content: "";
    width: 9px; height: 9px;
    border-radius: 50%;
    background: var(--ink);
    margin-right: 8px;
    align-self: center;
  }
  .appointment__row span { margin-right: 6px; }
  .appointment__line {
    flex: 1;
    border-bottom: 2px dotted var(--dots);
  }
  /* Front card */
  .card--front {
    top: 640px;
    background: var(--card-black);
    color: #fff;
    padding: 40px 46px;
  }
  .front__dentist { text-align: right; }
  .dentist-name { font-size: 34px; color: var(--sage-text); }
  .dentist-quals { font-size: 20px; letter-spacing: 1px; margin-top: 2px; }
  .dentist-phone { font-size: 20px; letter-spacing: 1px; margin-top: 4px; }
  .dentist-phone svg { vertical-align: -3px; margin-right: 6px; }
  .front__brand {
    position: absolute;
    right: 46px;
    bottom: 110px;
    text-align: right;
  }
  .front__brand .brand-name {
    font-size: 34px;
    color: var(--sage-text);
    padding-bottom: 8px;
    border-bottom: 1px solid var(--silver);
  }
</style>
</head>
<body>

<section class="card card--back">
  <div class="back__info">
    <div class="brand-name">Harbourlight Dental<br>Centre Kelvale</div>

    <div class="contact-item">
      <svg width="26" height="24" viewBox="0 0 26 24" aria-hidden="true">
        <path d="M13 2 L1 12 H5 V22 H11 V15 H15 V22 H21 V12 H25 Z" fill="#1b1b1b"/>
      </svg>
      117C, 58 Tarrow Street<br>Kelvale - 4561, Queensland
    </div>

    <div class="contact-item">
      <svg width="22" height="22" viewBox="0 0 22 22" aria-hidden="true">
        <circle cx="11" cy="11" r="10" fill="#1b1b1b"/>
      </svg>
      www.harbourlightdental.example.au
    </div>

    <div class="contact-item">
      <svg width="26" height="20" viewBox="0 0 26 20" aria-hidden="true">
        <path d="M1 8 L13 1 L25 8 V19 H1 Z" fill="#1b1b1b"/>
        <path d="M3 9 L13 15 L23 9" fill="none" stroke="#9cc383" stroke-width="1.5"/>
      </svg>
      admin@harbourlightdentalkelvale.example.au
    </div>
  </div>

  <div class="back__appointment">
    <h2 class="appointment__title">Next Appointment</h2>
    <div class="appointment__row"><span>Date</span><i class="appointment__line"></i></div>
    <div class="appointment__row"><span>Time</span><i class="appointment__line"></i></div>
    <div class="appointment__row"><span>Date</span><i class="appointment__line"></i></div>
    <div class="appointment__row"><span>Time</span><i class="appointment__line"></i></div>
    <div class="appointment__row"><span>Date</span><i class="appointment__line"></i></div>
    <div class="appointment__row"><span>Time</span><i class="appointment__line"></i></div>
  </div>
</section>

<section class="card card--front">
  <div class="front__dentist">
    <div class="dentist-name">Dr Anjali R Venkatesan</div>
    <div class="dentist-quals">B.D.S., M.P.H (Melb)</div>
    <div class="dentist-phone">
      <svg width="18" height="18" viewBox="0 0 24 24" aria-hidden="true">
        <path d="M6.6 10.8a15.1 15.1 0 0 0 6.6 6.6l2.2-2.2a1 1 0 0 1 1-.25 11.4 11.4 0 0 0 3.6.57 1 1 0 0 1 1 1V20a1 1 0 0 1-1 1A17 17 0 0 1 3 4a1 1 0 0 1 1-1h3.5a1 1 0 0 1 1 1c0 1.25.2 2.45.57 3.57a1 1 0 0 1-.25 1z" fill="#9cc383"/>
      </svg>07- 5918 2243
    </div>
  </div>

  <div class="front__brand">
    <div class="brand-name">Harbourlight Dental<br>Centre Kelvale</div>
  </div>
</section>

</body>
</html>
```